Corporate Notepads

We currently have a basic notepad with our logo and icon at the top along with contact information at the bottom. We want to come up with something more creative and jazz it up a bit. We are looking for unique ideas to make the notepads look nice and corporate possibly with watermarked look. We will take any ideas and choose the one that works best for the look. We have a website where you can get ideas about our company. Attached is the current simple notepad design we have right now.

```html
<!DOCTYPE html>
<html lang="en">
<head>
<meta charset="utf-8">
<title>Harlow Construction Notepad</title>
<link href="https://fonts.googleapis.com/css2?family=Montserrat:wght@500;600;700&display=swap" rel="stylesheet">
<style>
  :root {
    --navy: #3a4670;
    --navy-soft: #56618a;
    --lavender: #c7cbe6;
    --lavender-light: #e4e6f4;
    --paper: #ffffff;
    --ink-grey: #6d7186;
    --backdrop: #eef0f4;
  }
  * { margin: 0; padding: 0; box-sizing: border-box; }
  html, body {
    width: 1200px;
    height: 2452px;
    overflow: hidden;
    background: var(--backdrop);
    font-family: "Montserrat", sans-serif;
  }
  .notepad-sheet {
    position: absolute;
    left: 0; top: 0;
    width: 1200px;
    height: 2452px;
    background:
      linear-gradient(160deg, var(--lavender-light) 0%, rgba(255,255,255,0) 22%),
      linear-gradient(200deg, rgba(199,203,230,0.55) 0%, rgba(255,255,255,0) 30%),
      linear-gradient(20deg, var(--lavender) 0%, rgba(255,255,255,0) 38%),
      linear-gradient(340deg, rgba(199,203,230,0.8) 0%, rgba(255,255,255,0) 34%),
      var(--paper);
  }
  .sheet-header {
    position: absolute;
    top: 110px; left: 90px; right: 90px;
    display: flex;
    justify-content: space-between;
    align-items: flex-start;
  }
  .brand {
    display: flex;
    align-items: center;
    gap: 22px;
  }
  .brand-square {
    width: 92px; height: 92px;
    background: var(--navy);
  }
  .brand-name {
    font-weight: 700;
    color: var(--navy);
    line-height: 1.02;
    text-transform: uppercase;
  }
  .brand-name .line-main { display: block; font-size: 62px; letter-spacing: 1px; }
  .brand-name .line-sub { display: block; font-size: 25px; letter-spacing: 4px; }
  .contact-list {
    list-style: none;
    padding-top: 6px;
  }
  .contact-item {
    display: flex;
    align-items: center;
    gap: 16px;
    font-size: 22px;
    font-weight: 600;
    color: var(--navy-soft);
    letter-spacing: 1px;
    margin-bottom: 18px;
  }
  .contact-icon {
    width: 30px; height: 30px;
    background: var(--navy);
    border-radius: 4px;
    display: flex; align-items: center; justify-content: center;
  }
  .sheet-footer {
    position: absolute;
    left: 0; right: 0; bottom: 90px;
    display: flex;
    flex-direction: column;
    align-items: center;
    gap: 44px;
  }
  .footer-square {
    width: 70px; height: 70px;
    background: var(--navy-soft);
    opacity: 0.85;
  }
  .services-line {
    font-size: 22px;
    font-weight: 600;
    letter-spacing: 8px;
    color: var(--ink-grey);
    text-transform: uppercase;
  }
</style>
</head>
<body>
  <main class="notepad-sheet">
    <header class="sheet-header">
      <div class="brand">
        <div class="brand-square"></div>
        <div class="brand-name">
          <span class="line-main">Harlow</span>
          <span class="line-sub">Construction</span>
        </div>
      </div>
      <ul class="contact-list">
        <li class="contact-item">
          <span class="contact-icon">
            <svg width="18" height="18" viewBox="0 0 24 24" aria-hidden="true">
              <path fill="#fff" d="M6.6 10.8a15 15 0 0 0 6.6 6.6l2.2-2.2c.3-.3.7-.4 1-.2 1.1.4 2.3.6 3.6.6.6 0 1 .4 1 1V20c0 .6-.4 1-1 1C10.6 21 3 13.4 3 4c0-.6.4-1 1-1h3.5c.6 0 1 .4 1 1 0 1.3.2 2.5.6 3.6.1.3 0 .7-.2 1z"/>
            </svg>
          </span>
          555-214-0187
        </li>
        <li class="contact-item">
          <span class="contact-icon">
            <svg width="18" height="18" viewBox="0 0 24 24" aria-hidden="true">
              <circle cx="12" cy="12" r="8.5" fill="none" stroke="#fff" stroke-width="2"/>
              <path d="M3.5 12h17M12 3.5c2.8 3 2.8 14 0 17M12 3.5c-2.8 3-2.8 14 0 17" fill="none" stroke="#fff" stroke-width="1.6"/>
            </svg>
          </span>
          harlowbuilders.com
        </li>
      </ul>
    </header>

    <footer class="sheet-footer">
      <div class="footer-square"></div>
      <p class="services-line">Civil &bull; Industrial &bull; Commercial</p>
    </footer>
  </main>
</body>
</html>
```